Poster for a Bicycle show/Expo

We need a poster for a Bicycle show/Expo and sustainable transport. Exhibitors will sell bikes, cycling clothing, accessories, etc. ...
This show is annual and the Poster is for the 2015 edition.

The style must be modern, dynamic, bright colors.

Your concept must be compatible in a landscape format. (We will ourselves adaptations of different formats.)
Width: 210 mm
Height: 297 mm
It's necessary for us to have the source file (vector) for make, later, the different format (flyers, website, ...)

Content of the Poster:
- 1 big picture (no clip art)
- Big title: « Fête Roulix » (« Salon » or « Salon du » can be small and « Vélo » big.)
- Subtitle: « et de la mobilité douce »
- Date: « 8, 9 et 10 mai 2015 » or « 8-10 mai 2015 »
- Place: « Halle TRX - Quai Brenaz »
- Text line 1: « www.fete-roulix.ch - Entrée gratuite »
- Text line 2« Piste d’essais - Restauration sur place »
- Text line 3: « Ve 8 mai de 17h à 21h - Sa 9 mai de 10h à 20h - Di 10 mai de 10h à 18h »
- Please, leave a zone in the poster for sponsors logos
(The predominant information (most visible) are: « Fête Roulix » and « 8, 9 et 10 mai 2015 or 8-10 mai 2015 »)

Content of the big picture:
- from a cheap stock, like PixoBanq.com
- a bicycle in action or a detail of a bicycle (or a accessory) (no race bike)
- a modern picture with bright colors.
- if a person is on the picture, we prefer a men
- not an aerial view with cyclists in a landscape.

Some examples of poster of shows - with typo-title worked

http://www.bassinexpoville.com/Temp/IMG/F_a7c2e9b4d1f0836255e1b7a9c4d3f2e6812c9b0a4e5f7_200_296.png

http://qz4m.tolvanfoires.fr/Data/kmtolv_mer/block/F_9bd1c3e7f2a4605813c9e2d7b4a8f6c0d3e1a527f86c2.pdf
(page 2 of this PDF)

http://salons.marvelle-agenda.fr/images/marvelle-agenda/foires-salons/phototheque/expo-moto-brivanne/expo-moto-brivanne2012-affiche.jpg

http://www.drupaix.net/blog/wp-content/uploads/2007/03/affiche-foire-des-pages.jpg

http://www.voilemarine-club.com/wp-content/affiche-regate-2007.jpg

Hello,

For information, for your next versions, please, add the text "Piste d'essais".

- Text line 1: « www.fete-roulix.ch - Entrée gratuite »
- Text line 2: « Piste d’essais - Restauration sur place »
- Text line 3: « Ve 8 mai de 17h à 21h - Sa 9 mai de 10h à 20h - Di 10 mai de 10h à 18h »

Thanks,
Mathieu

Landscape

Sans Serif

```html
<!DOCTYPE html>
<html lang="fr">
<head>
<meta charset="utf-8">
<title>Fête Roulix et de la mobilité douce — 8, 9 et 10 mai 2015</title>
<link rel="stylesheet" href="https://fonts.googleapis.com/css2?family=Arimo:wght@700&family=Source+Sans+3:wght@400;500&display=swap">
<style>
  :root {
    --cyan: #00a9e6;
    --plum: #a24f8e;
    --orange: #f28a2e;
    --white: #ffffff;
    --photo-light: #e9ddd0;
    --photo-mid: #b9a48f;
    --photo-dark: #3a332e;
    --photo-warm: #c99a63;
  }
  * { margin: 0; padding: 0; box-sizing: border-box; }
  html, body { width: 1200px; height: 849px; overflow: hidden; background: var(--white); }
  .poster {
    position: relative;
    width: 1200px;
    height: 849px;
    overflow: hidden;
    font-family: "Source Sans 3", "Helvetica Neue", Arial, sans-serif;
  }
  .poster__photo {
    position: absolute;
    inset: 0;
    background:
      radial-gradient(ellipse 420px 380px at 300px 260px, rgba(58,51,46,0.0) 55%, rgba(58,51,46,0.55) 62%, rgba(58,51,46,0) 68%),
      radial-gradient(ellipse 380px 420px at 1010px 330px, rgba(58,51,46,0) 50%, rgba(58,51,46,0.6) 58%, rgba(58,51,46,0) 66%),
      radial-gradient(ellipse 260px 200px at 900px 180px, rgba(58,51,46,0.55), rgba(58,51,46,0) 70%),
      linear-gradient(90deg, var(--photo-light) 0%, var(--photo-mid) 45%, var(--photo-warm) 75%, var(--photo-mid) 100%);
  }
  .title {
    position: absolute;
    left: 0;
    top: 0;
    color: var(--cyan);
    font-family: "Arimo", Arial, sans-serif;
    font-weight: 700;
    line-height: 1;
  }
  .title__lead {
    position: absolute;
    left: 96px;
    top: 420px;
    font-size: 112px;
    letter-spacing: -2px;
    white-space: nowrap;
  }
  .title__main {
    position: absolute;
    left: 338px;
    top: 350px;
    font-size: 206px;
    letter-spacing: -6px;
    white-space: nowrap;
  }
  .band {
    position: absolute;
    left: 644px;
    width: 466px;
    background: var(--plum);
    color: var(--white);
    text-align: right;
    padding-right: 18px;
  }
  .band--subtitle {
    top: 537px;
    height: 41px;
    font-size: 29px;
    line-height: 41px;
  }
  .band--event {
    top: 586px;
    height: 82px;
    padding-top: 6px;
  }
  .event__date {
    font-size: 30px;
    line-height: 34px;
  }
  .event__date small { font-size: 20px; }
  .event__date .event__month { font-size: 20px; }
  .event__place {
    font-size: 20px;
    line-height: 34px;
  }
  .event__place::before { content: "\00BB"; font-weight: 500; margin-right: 8px; }
  .info {
    position: absolute;
    top: 677px;
    height: 81px;
    width: 268px;
    background: var(--orange);
    color: var(--white);
    font-size: 19.5px;
    line-height: 22px;
    padding-top: 7px;
    text-align: center;
  }
  .info--access { left: 90px; }
  .info--hours { left: 368px; }
  .sponsors {
    position: absolute;
    left: 644px;
    top: 677px;
    width: 466px;
    height: 81px;
    background: var(--white);
  }
</style>
</head>
<body>
<main class="poster">
  <div class="poster__photo" role="img" aria-label="Photographie en gros plan d'une roue arrière de vélo avec pédalier, dérailleur et béquille sur des pavés clairs"></div>

  <h1 class="title">
    <span class="title__lead">Fête</span>
    <span class="title__main">ROULIX</span>
  </h1>

  <p class="band band--subtitle">et de la mobilité douce</p>

  <div class="band band--event">
    <p class="event__date">8<small>,</small> 9 <small>et</small> 10 <span class="event__month">MAI 2015</span></p>
    <p class="event__place">Halle TRX - Quai Brenaz</p>
  </div>

  <div class="info info--access">
    <p>www.fete-roulix.ch</p>
    <p>Entrée gratuite</p>
    <p>Restauration sur place</p>
  </div>

  <div class="info info--hours">
    <p>Ve 8 mai de 17h à 21h</p>
    <p>Sa 9 mai de 10h à 20h</p>
    <p>Di 10 mai de 10h à 18h</p>
  </div>

  <div class="sponsors" aria-label="Espace partenaires"></div>
</main>
</body>
</html>
```